Business Card for premium dental clinic

We are a premium dental clinic based in Brasov, Romania with more than 15 year on the market, providing quality dental treatment made by a team of more specialized dentists, working with modern equipment as a solution to beautiful and healthy teeth.

Our current logo for the clinic use 2 square with colors black and gold - dr Corbescu - studio, using family fonts Bodoni, Myriad Pro and Segoe Print.
Depending on the printing we used some gold CMYK background or gold foil picture background or a gold gradient.
We want a business card:
- eye catching business card
- distinguished business card
- premium design
- to keep the color scheme of black and gold
- to attract the customers to spent time reading the information
- modern concept

```html
<!DOCTYPE html>
<html lang="en">
<head>
<meta charset="utf-8">
<title>dr Corbescu – Business Card</title>
<link rel="stylesheet" href="https://fonts.googleapis.com/css2?family=Montserrat:wght@400;600&display=swap">
<style>
  :root {
    --stage: #e9e6e1;
    --charcoal: #2a2d2f;
    --gold: #c9a02b;
    --gold-light: #f2d35a;
    --gold-deep: #b8891a;
    --black: #0b0b0b;
    --paper: #f7f7f5;
    --ink: #3a3a3a;
    --white: #ffffff;
  }
  * { margin: 0; padding: 0; box-sizing: border-box; }
  html, body { width: 1200px; height: 866px; overflow: hidden; }
  body {
    background: var(--stage);
    font-family: "Montserrat", sans-serif;
    display: flex;
    flex-direction: column;
    align-items: center;
    justify-content: center;
    gap: 48px;
  }
  .card {
    width: 620px;
    height: 354px;
    position: relative;
    overflow: hidden;
    box-shadow: 0 10px 28px rgba(0,0,0,0.18);
  }

  /* Front */
  .card--front { display: flex; }
  .front__dark { width: 40%; background: var(--charcoal); }
  .front__gold { flex: 1; background: var(--gold); }
  .front__mark { position: absolute; left: 50%; top: 50%; transform: translate(-50%, -50%); }

  /* Mark block */
  .mark {
    display: flex;
    border: 3px solid var(--white);
    background: var(--white);
  }
  .mark__foil {
    background: linear-gradient(135deg, var(--gold-deep), var(--gold-light) 45%, var(--gold) 70%, var(--gold-light));
  }
  .mark__square {
    background: var(--black);
    display: flex;
    align-items: center;
    justify-content: center;
    gap: 10px;
  }
  .mark__name {
    color: var(--white);
    font-weight: 600;
    letter-spacing: 0.02em;
    white-space: nowrap;
  }
  .mark--large .mark__foil { width: 200px; height: 170px; }
  .mark--large .mark__square { width: 200px; height: 170px; }
  .mark--large .mark__name { font-size: 22px; }
  .mark--small .mark__foil { width: 130px; height: 110px; }
  .mark--small .mark__square { width: 130px; height: 110px; }
  .mark--small .mark__name { font-size: 15px; }

  /* Back */
  .card--back { background: var(--paper); display: flex; align-items: center; }
  .back__mark { margin-left: 36px; }
  .back__rule { width: 2px; height: 196px; background: var(--gold); margin: 0 26px 0 30px; }
  .back__info { color: var(--ink); font-size: 12.5px; line-height: 1.45; }
  .person__name { color: var(--gold); font-size: 22px; font-weight: 600; line-height: 1.1; }
  .person__role { font-size: 13px; margin-bottom: 16px; }
  .address { margin-bottom: 14px; }
  .contacts { list-style: none; }
  .contacts li { display: flex; align-items: center; gap: 10px; }
  .contacts svg { width: 13px; height: 13px; flex: none; fill: var(--gold); }
</style>
</head>
<body>

  <section class="card card--front" aria-label="Card front">
    <div class="front__dark"></div>
    <div class="front__gold"></div>
    <div class="front__mark">
      <div class="mark mark--large">
        <div class="mark__foil" role="img" aria-label="Gold foil texture"></div>
        <div class="mark__square"><span class="mark__name">dr Corbescu</span></div>
      </div>
    </div>
  </section>

  <section class="card card--back" aria-label="Card back">
    <div class="back__mark">
      <div class="mark mark--small">
        <div class="mark__foil" role="img" aria-label="Gold foil texture"></div>
        <div class="mark__square"><span class="mark__name">dr Corbescu</span></div>
      </div>
    </div>
    <div class="back__rule"></div>
    <div class="back__info">
      <p class="person__name">Maria Stanescu</p>
      <p class="person__role">Doctor</p>
      <p class="address">Strada Lungă nr 24<br>500058 Brașov</p>
      <ul class="contacts">
        <li>
          <svg viewBox="0 0 16 16" aria-hidden="true"><path d="M4 1h8a1 1 0 0 1 1 1v12a1 1 0 0 1-1 1H4a1 1 0 0 1-1-1V2a1 1 0 0 1 1-1zm1 2v9h6V3zm3 10a.8.8 0 1 0 0 .01z"/></svg>
          601-555-0147
        </li>
        <li>
          <svg viewBox="0 0 16 16" aria-hidden="true"><path d="M3.6 1.5l2.3-.5 1.4 3.3-1.6 1.2a8 8 0 0 0 4.8 4.8l1.2-1.6 3.3 1.4-.5 2.3A2 2 0 0 1 12.6 14 11 11 0 0 1 2 3.4a2 2 0 0 1 1.6-1.9z"/></svg>
          +40 268 555 019
        </li>
        <li>
          <svg viewBox="0 0 16 16" aria-hidden="true"><path d="M1 3h14v10H1zm1.5 1.3V12h11V4.3L8 8.6z M2.8 4 8 7.9 13.2 4z"/></svg>
          m.stanescu@drcorbescu.ro
        </li>
        <li>
          <svg viewBox="0 0 16 16" aria-hidden="true"><path d="M8 1a7 7 0 1 0 0 14A7 7 0 0 0 8 1zm0 1.4c.8.9 1.4 2.3 1.6 4H6.4C6.6 4.7 7.2 3.3 8 2.4zM2.5 7.4h2.5c0 1.5.3 2.9.8 4A5.6 5.6 0 0 1 2.5 7.4zm0-.9a5.6 5.6 0 0 1 3.3-3.9c-.5 1.1-.8 2.4-.8 3.9zm5.5 7.1c-.8-.9-1.4-2.3-1.6-4h3.2c-.2 1.7-.8 3.1-1.6 4zm2.2-.8c.5-1.1.8-2.4.8-4h2.5a5.6 5.6 0 0 1-3.3 4zm.8-4.9c0-1.5-.3-2.8-.8-3.9a5.6 5.6 0 0 1 3.3 3.9z"/></svg>
          www.drcorbescu.ro
        </li>
      </ul>
    </div>
  </section>

</body>
</html>
```